Give Tall Oak Ridge an Online Presence!

Tall Oak Ridge Property Maintenance is an Australian Owned property maintenance company who needs a stand out online presence.

TOR maintains many buildings and sites and wants to appeal to a corporate professional market with their brand new website. TOR is essentially a handyman service offering all maintenance services to home owners, office managers, real estate agents and strata managers.

The Website:
We need a corporate website that appeals to our broader customer base (property owners, property managers, office managers) the copy is being written by a professional so use filler text for now.

Things that we want:
Home page that sets us apart and appeals to the corporate and residential market. The home page needs to not focus on either the residential or commercial market. The home page should focus on our logo and branding. We have a logo already and it is attached to the brief, please use it and try to consider the colour pallette that goes with it. Whilst we want the site to appear strong and manly it is important to remember that 95% of our customers are female so we need the site to be appealing to women. Women need to believe that we are strong, dependable and trustworthy.
We'd like a quote page and potentially also the ability to get a quote from the home page (please don't put it in if it ruins the overall feel of the home page)
An "about us" page
A contact us page
A blog that's built in (we don't want to link to an external blog)
(overall we'd expect to have 6 or 7 pages total)

The site will also need coding - we expect this to be done in a separate project but need you to consider a few things about the coding side of things.

It needs to be iPhone and iPad compatible.

We'd like you to suggest the best CMS that you would use or if you would suggest not using a CMS please let us know with your submissions.

Target Market(s)

Property owners, office managers and property managers who need maintenance on buildings (So all of them)

Industry/Entity Type

Property Maintenance

Requirements
Must have
• Our Logo
Home page
About Us
Residential
Commercial
Real Estate/Strata
Contact Us/Quote
Blog
Nice to have
• Quote form included in home page
Movement on the home page at least
Should not have
• other logos, too much colour
NO FLASH

```html
<!DOCTYPE html>
<html lang="en">
<head>
<meta charset="utf-8">
<title>Tall Oak Ridge Property Maintenance</title>
<link rel="stylesheet" href="https://fonts.googleapis.com/css2?family=Ubuntu:wght@500;700&family=Arimo:wght@400;700&family=Noto+Sans:wght@400&display=swap">
<style>
:root{
  --orange:#f7901e;
  --orange-deep:#e57f10;
  --orange-light:#ffd59a;
  --black:#000;
  --ink:#2a1a05;
  --text:#4a4a4a;
  --page:#fafafa;
  --white:#fff;
  --yellow:#ffd800;
  --social:#1b2a3a;
}
*{margin:0;padding:0;box-sizing:border-box}
html,body{width:1200px;height:1156px;overflow:hidden;background:var(--page)}
body{position:relative;font-family:"Arimo",Arial,sans-serif}
.top-bar{position:absolute;left:0;top:0;width:1200px;height:84px;background:var(--orange)}
.brand{position:absolute;left:176px;top:20px;color:var(--white);font-family:"Ubuntu",sans-serif;font-weight:700;line-height:1}
.brand .name{font-size:27px;letter-spacing:-0.3px}
.brand .sub{font-size:15px;margin-top:3px}
.contact-box{position:absolute;left:556px;top:10px;width:469px;height:64px;border:1px solid var(--orange-light);border-radius:8px}
.give-line{position:absolute;left:46px;top:13px;color:var(--orange-light);font-size:15px}
.send-btn{position:absolute;left:13px;top:32px;width:114px;height:22px;border-radius:8px;background:#1a1a1a;color:var(--white);font-weight:700;font-size:14px;text-align:center;line-height:22px}
.envelope{position:absolute;left:137px;top:9px}
.phone-icon{position:absolute;left:234px;top:9px}
.say-hello{position:absolute;left:289px;top:18px;color:var(--orange-light);font-size:15px}
.phone-number{position:absolute;left:289px;top:33px;color:var(--white);font-size:24px;font-weight:700;letter-spacing:0.5px}
.main-nav{position:absolute;left:0;top:84px;width:1200px;height:54px;background:var(--black)}
.main-nav a{position:absolute;top:0;height:54px;line-height:54px;color:var(--white);font-size:15px;text-decoration:none}
.main-nav a.active{background:var(--orange);padding:0 13px;left:173px}
.hero{position:absolute;left:0;top:138px;width:1200px;height:355px;background:radial-gradient(ellipse at 50% 45%,#5a5a5a 0%,#2c2c2c 35%,#0b0b0b 70%,#000 100%)}
.hero svg{position:absolute;left:0;top:0}
.crew-art{position:absolute;left:480px;top:42px;width:260px;height:222px;background:linear-gradient(180deg,#1b1b1b 0%,#111 60%,var(--orange) 100%);border-radius:60px 60px 4px 4px;opacity:.9}
.hero-badge{position:absolute;left:457px;top:252px;width:285px;height:59px;background:var(--orange);border-radius:10px;color:var(--white);font-family:"Ubuntu",sans-serif;font-weight:700;text-align:center;line-height:1}
.hero-badge .name{font-size:26px;margin-top:5px}
.hero-badge .sub{font-size:19px;margin-top:3px}
.hero-strip{position:absolute;left:0;top:493px;width:1200px;height:42px;background:linear-gradient(180deg,#1e1206 0%,var(--orange-deep) 60%,var(--orange) 100%)}
.service-card{position:absolute;top:590px;width:257px;height:182px;background:var(--white);border:1px solid var(--orange);padding:16px 14px 0 16px;box-shadow:0 8px 8px -6px rgba(0,0,0,.45)}
.service-card h2{font-family:"Arimo",sans-serif;font-weight:400;font-size:19px;color:var(--orange);letter-spacing:.3px}
.service-card p{font-family:"Noto Sans",Verdana,sans-serif;font-size:13.6px;line-height:18px;color:var(--text);margin-top:3px;letter-spacing:.2px}
.clients-title{position:absolute;left:194px;top:838px;font-size:23px;font-weight:400;color:#111;font-family:"Noto Sans",sans-serif}
.client{position:absolute;top:812px;width:161px;height:80px;display:flex;align-items:center;justify-content:center;font-family:"Arimo",sans-serif;font-weight:700;font-size:19px}
.client-1{left:347px;background:linear-gradient(135deg,#4fc3ec,#1e95d4);color:var(--white)}
.client-2{left:520px;background:#050505;border:2px solid var(--orange);color:var(--orange)}
.client-3{left:694px;background:linear-gradient(180deg,#fff,#e4e4e4);color:#c1272d;border:1px solid #ddd}
.client-4{left:867px;background:linear-gradient(180deg,#f6c800 0 30%,#3b7fa5 30%,#8a5fb0 100%);color:var(--black)}
.site-footer{position:absolute;left:173px;top:927px;width:855px;height:135px;background:var(--orange);box-shadow:0 14px 12px -8px rgba(0,0,0,.55)}
.skills{position:absolute;left:17px;top:13px;font-size:19px;font-weight:700;line-height:24px;color:var(--ink)}
.office{position:absolute;left:301px;top:13px;color:var(--ink)}
.office h3,.newsletter h3{font-size:19px;font-weight:700}
.office p{font-size:13px;line-height:17px;margin-top:5px}
.newsletter{position:absolute;left:584px;top:13px;width:256px;color:var(--ink)}
.signup{position:absolute;left:0;top:31px;width:252px;height:36px;border:2px solid var(--yellow);background:var(--white);display:flex}
.signup span{flex:1;font-size:13px;line-height:32px;padding-left:10px;color:#333}
.signup b{width:104px;background:var(--yellow);font-size:14px;line-height:32px;padding-left:10px}
.social{position:absolute;top:84px;height:34px;border-radius:4px;background:var(--social);color:var(--white);font-size:11px;font-weight:700;line-height:34px;padding:0 7px}
.copyright{position:absolute;left:0;top:1097px;width:1200px;text-align:center;font-size:12px;font-weight:700;color:#555}
</style>
</head>
<body>
<header class="top-bar">
  <div class="brand"><div class="name">TALL OAK RIDGE</div><div class="sub">PROPERTY MAINTENANCE</div></div>
  <div class="contact-box">
    <span class="give-line">Give a line</span>
    <span class="send-btn">Send Message</span>
    <svg class="envelope" width="58" height="46" viewBox="0 0 58 46"><rect x="1" y="4" width="56" height="38" fill="#fbfbfb" stroke="#ccc"/><path d="M1 4 L29 26 L57 4" fill="none" stroke="#bbb" stroke-width="2"/></svg>
    <svg class="phone-icon" width="52" height="46" viewBox="0 0 52 46"><path d="M4 14 Q26 0 48 14 L44 20 L36 16 L16 16 L8 20 Z" fill="#1a1a1a"/><rect x="10" y="20" width="32" height="22" rx="4" fill="#1a1a1a"/><circle cx="26" cy="29" r="8" fill="#f7901e"/><circle cx="26" cy="29" r="3" fill="#1a1a1a"/></svg>
    <span class="say-hello">Say Hello</span>
    <span class="phone-number">0400 555 019</span>
  </div>
</header>
<nav class="main-nav">
  <a class="active" href="#">HOME</a>
  <a href="#" style="left:258px">ABOUT US</a>
  <a href="#" style="left:361px">RESIDENTIAL</a>
  <a href="#" style="left:485px">COMMERCIAL</a>
  <a href="#" style="left:609px">REAL ESTATE/STRATA</a>
  <a href="#" style="left:794px">CONTACT US/QUOTE</a>
  <a href="#" style="left:970px">BLOG</a>
</nav>
<section class="hero">
  <div class="crew-art" role="img" aria-label="Silhouettes of three tradesmen standing above a city skyline"></div>
  <div class="hero-badge"><div class="name">TALL OAK RIDGE</div><div class="sub">PROPERTY MAINTENANCE</div></div>
  <svg width="1200" height="355" viewBox="0 0 1200 355" font-family="Arimo, Arial, sans-serif" font-size="11" font-weight="700" fill="#fff">
    <g stroke="#f7901e" stroke-width="2" fill="none">
      <path d="M281 84 H433 L452 104"/><path d="M271 138 H415 L433 156"/>
      <path d="M272 191 H411 L431 208"/><path d="M218 238 H394 L412 255"/>
      <path d="M335 282 H395 L412 299"/>
      <path d="M810 45 H752 L734 63"/><path d="M850 82 H770 L752 99"/>
      <path d="M897 121 H775 L755 138"/><path d="M897 156 H793 L774 173"/>
      <path d="M871 194 H793 L776 211"/><path d="M856 232 H803 L782 249"/>
      <path d="M856 272 H803 L784 290"/>
    </g>
    <g fill="#f7901e" stroke="#7a4a10" stroke-width="3">
      <circle cx="452" cy="104" r="4"/><circle cx="433" cy="156" r="4"/><circle cx="431" cy="208" r="4"/>
      <circle cx="412" cy="255" r="4"/><circle cx="412" cy="299" r="4"/>
      <circle cx="734" cy="63" r="4"/><circle cx="752" cy="99" r="4"/><circle cx="755" cy="138" r="4"/>
      <circle cx="774" cy="173" r="4"/><circle cx="776" cy="211" r="4"/><circle cx="782" cy="249" r="4"/>
      <circle cx="784" cy="290" r="4"/>
    </g>
    <text x="281" y="66">All commercial and</text><text x="281" y="80">residential handyman work</text>
    <text x="271" y="132">Strata management work</text>
    <text x="272" y="185">Scheduled maintenance</text>
    <text x="218" y="232">Pictures and whiteboards hung</text>
    <text x="335" y="276">Lighting</text>
    <text x="752" y="39">Carpentry</text>
    <text x="770" y="76">Doors and locks</text>
    <text x="775" y="115">Windows and screens</text>
    <text x="793" y="150">Furniture assembly</text>
    <text x="793" y="188">Office moves</text>
    <text x="803" y="226">Painting</text>
    <text x="803" y="266">All repairs</text>
  </svg>
</section>
<div class="hero-strip"></div>
<main>
  <article class="service-card" style="left:173px"><h2>RESIDENTIAL</h2><p>By nerds, for nerds.<br>Built at Flitter by @ash and @elm, Framekit utilizes TIDE CSS, is compiled via Knot, and is managed through Repobay to help nerds do awesome stuff on the web.</p></article>
  <article class="service-card" style="left:475px"><h2>COMMERCIAL</h2><p>By nerds, for nerds.<br>Built at Flitter by @ash and @elm, Framekit utilizes TIDE CSS, is compiled via Knot, and is managed through Repobay to help nerds do awesome stuff on the web.</p></article>
  <article class="service-card" style="left:771px"><h2>REAL ESTATE/STRATA</h2><p>By nerds, for nerds.<br>Built at Flitter by @ash and @elm, Framekit utilizes TIDE CSS, is compiled via Knot, and is managed through Repobay to help nerds do awesome stuff on the web.</p></article>
  <h2 class="clients-title">Our Clients</h2>
  <div class="client client-1">Formwell</div>
  <div class="client client-2">Draftline</div>
  <div class="client client-3">Vertex Studio</div>
  <div class="client client-4">Meshwork</div>
</main>
<footer class="site-footer">
  <p class="skills">Cross functional skills set<br>of Mechanical Engineering,<br>Industrial Design,<br>Mechanical Trade<br>and Graphic Design.</p>
  <div class="office">
    <h3>Head Office</h3>
    <p>Address 14 Ridgeline Road<br>Oakvale NSW 2290<br>Phone 02 4900 0172<br>Email hello@talloakridge.example<br>Web www.talloakridge.example</p>
  </div>
  <div class="newsletter">
    <h3>Join Our News Letter</h3>
    <div class="signup"><span>Your Email Address</span><b>Subscribe ›</b></div>
    <span class="social" style="left:0">Sketchly</span>
    <span class="social" style="left:64px">Friendbook</span>
    <span class="social" style="left:146px">Workline</span>
  </div>
</footer>
<p class="copyright">Copyright 2011 © TOR Property Maintenance - All Rights Reserved</p>
</body>
</html>
```